Banner Design for Brisk Loans

Hi,

I know this is under flyer design, however, I am actually after a Banner (I could not find this option). The banner needs to be done to fit the following specifications.

1 x 850mm W x 1500mm H Double Sided Luxury Retractable

I have provided a banner which I currently have however, I would like it to be updated.

I would like to banners created.

Banner 1

The banner should still maintain the lender logos and the fact we assess over 30 lenders, plus also promote the 'Brisk Loans' logo.

Along with this is I would like to promote the 'Brisk Cost Refund.'

Also have the wording
'We Cover your Discharge fee and new loan application fee'
also may use this link as guidance http://www.briskloansdemo.com.au/briskrefund/

Banner 2

This banner I would like it to promote a 'Quick Mortgage Health Check'.

Also include 'The Brisk Loans Edge'

http://www.briskloansdemo.com.au/briskrefund/

Again use this as a guide as to the 4 points of difference, you may use different icons if you feel it looks better

Target Market(s)

People with Home Loans

Industry/Entity Type

Finance

Font styles to use
Sans Serif

Colors
ec1f27
ffffff

Requirements
Must have
• As per the description
Nice to have
• Professional look, good icons to accompany wording
Should not have
• unprofessional look too much text or cluttered

```html
<!DOCTYPE html>
<html lang="en">
<head>
<meta charset="utf-8">
<title>Brisk Loans Banners</title>
<link rel="stylesheet" href="https://fonts.googleapis.com/css2?family=Montserrat:wght@500;600;700;800&family=Didact+Gothic&family=Open+Sans:wght@600;700&display=swap">
<style>
:root{
  --brand-red:#ec1f27;
  --ink:#111111;
  --paper:#ffffff;
  --stage:#dcdcdc;
  --muted:#333333;
}
*{box-sizing:border-box;margin:0;padding:0}
html,body{width:1200px;height:1200px;overflow:hidden;background:var(--stage)}
.stage{position:relative;width:1200px;height:1200px}
.banner{position:absolute;top:74px;width:560px;height:1052px;background:var(--paper);overflow:hidden;box-shadow:0 4px 14px rgba(0,0,0,.25)}
.banner--refund{left:20px}
.banner--health{left:620px}
.brand{position:absolute;left:0;top:0;width:100%;height:222px;display:flex;flex-direction:column;align-items:center;justify-content:flex-end;padding-bottom:22px}
.brand__name{display:flex;align-items:center;gap:12px;font-family:"Montserrat",sans-serif;font-weight:600;font-size:38px;color:var(--ink);letter-spacing:.5px}
.brand__square{width:30px;height:30px;background:var(--brand-red)}
.brand__tagline{margin-top:8px;font-family:"Montserrat",sans-serif;font-weight:700;font-size:12px;color:var(--ink);letter-spacing:.3px}
.dark-panel{position:absolute;left:0;width:100%;background:var(--ink)}
.banner--refund .dark-panel{top:458px;height:307px}
.banner--health .dark-panel{top:222px;height:543px;border-top:5px solid var(--brand-red)}
.room-photo{position:absolute;left:21px;top:225px;width:517px;height:323px;background:linear-gradient(180deg,#8d8d8b 0%,#c9c7c2 45%,#b7b3ab 70%,#5c5a55 100%)}
.refund-flag{position:absolute;left:40px;top:313px;width:474px;height:147px;background:rgba(236,31,39,.82);display:flex;align-items:center;justify-content:center}
.refund-flag::after{content:"";position:absolute;inset:6px;border:1px solid rgba(255,255,255,.55)}
.refund-flag span{font-family:"Montserrat",sans-serif;font-weight:800;font-size:30px;color:var(--paper);letter-spacing:1px}
.cover-copy{position:absolute;left:0;width:100%;top:562px;text-align:center;color:var(--paper)}
.cover-copy__lead{font-family:"Didact Gothic",sans-serif;font-size:32px;letter-spacing:1px;line-height:46px}
.cover-copy__fee{font-family:"Montserrat",sans-serif;font-weight:600;font-size:50px;color:var(--brand-red);line-height:56px}
.cover-copy__amp{font-family:"Didact Gothic",sans-serif;font-size:30px;color:var(--paper)}
.cover-copy__loan{font-family:"Montserrat",sans-serif;font-weight:600;font-size:32px;line-height:48px;letter-spacing:.5px}
.rule{position:absolute;height:3px;background:var(--paper)}
.health-copy{position:absolute;left:0;width:100%;text-align:center;color:var(--paper)}
.health-copy__title{top:250px;font-family:"Montserrat",sans-serif;font-weight:800;font-size:56px;letter-spacing:3px;line-height:64px}
.health-copy__check{top:330px;font-family:"Montserrat",sans-serif;font-weight:700;font-size:32px;color:var(--brand-red);line-height:40px}
.health-copy__kicker{top:404px;font-family:"Montserrat",sans-serif;font-weight:500;font-size:26px;letter-spacing:8px;line-height:34px}
.health-copy__edge{top:438px;font-family:"Montserrat",sans-serif;font-weight:800;font-size:64px;line-height:72px;letter-spacing:1px}
.edge-list{position:absolute;top:558px;left:0;width:100%;display:grid;grid-template-columns:repeat(4,1fr);padding:0 14px;list-style:none}
.edge-item{display:flex;flex-direction:column;align-items:center;text-align:center;font-family:"Open Sans",sans-serif;font-weight:600;font-size:17px;line-height:22px;color:var(--paper)}
.edge-item svg{width:88px;height:88px;margin-bottom:8px}
.lenders-band{position:absolute;left:0;top:765px;width:100%;height:5px;background:var(--brand-red)}
.lenders-pill{position:absolute;left:77px;top:738px;width:405px;height:54px;border-radius:9px;background:var(--brand-red);display:flex;align-items:center;justify-content:center;font-family:"Open Sans",sans-serif;font-weight:700;font-size:25px;color:var(--paper);letter-spacing:.5px}
.lender-grid{position:absolute;left:36px;top:822px;width:488px;display:grid;grid-template-columns:repeat(5,1fr);row-gap:34px;column-gap:6px;list-style:none}
.lender{height:24px;display:flex;align-items:center;justify-content:center;text-align:center;font-family:"Open Sans",sans-serif;font-weight:700;font-size:12px;line-height:13px;color:var(--muted)}
.footer{position:absolute;left:0;top:1002px;width:100%;height:38px;background:var(--ink);border-top:4px solid var(--brand-red);display:flex;align-items:center;justify-content:center;font-family:"Didact Gothic",sans-serif;font-size:17px;color:var(--paper);letter-spacing:2px}
</style>
</head>
<body>
<main class="stage">

  <section class="banner banner--refund" aria-label="Brisk Cost Refund banner">
    <header class="brand">
      <div class="brand__name"><span class="brand__square"></span>Brisk Loans</div>
      <p class="brand__tagline">IS YOUR MORTGAGE IN GOOD SHAPE?</p>
    </header>
    <div class="dark-panel"></div>
    <div class="room-photo" role="img" aria-label="Photo of a modern living room with white sofas and a fireplace"></div>
    <div class="refund-flag"><span>BRISK COST REFUND</span></div>
    <div class="cover-copy">
      <p class="cover-copy__lead">WE COVER YOUR</p>
      <p class="cover-copy__fee">DISCHARGE FEE <span class="cover-copy__amp">&amp;</span></p>
      <p class="cover-copy__loan">NEW LOAN APPLICATION FEE</p>
    </div>
    <div class="rule" style="left:26px;width:507px;top:712px"></div>
    <div class="lenders-band"></div>
    <div class="lenders-pill">WE ASSESS OVER 30 LENDERS</div>
    <ul class="lender-grid">
      <li class="lender">Orbit Direct</li><li class="lender">Westvale Bank</li><li class="lender">Meadow Bank</li><li class="lender">Sunridge Bank</li><li class="lender">Wattle Bank</li>
      <li class="lender">Harbour Permanent</li><li class="lender">Cityline Bank</li><li class="lender">Homestead Loans</li><li class="lender">Paprika Lending</li><li class="lender">Blueprint Lending</li>
      <li class="lender">Commonfield Bank</li><li class="lender">Riverton Bank</li><li class="lender">Austral Bank</li><li class="lender">Northgate Bank</li><li class="lender">Legacy Bank</li>
    </ul>
    <footer class="footer">www.briskloansdemo.com.au</footer>
  </section>

  <section class="banner banner--health" aria-label="Mortgage Health Check banner">
    <header class="brand">
      <div class="brand__name"><span class="brand__square"></span>Brisk Loans</div>
      <p class="brand__tagline">IS YOUR MORTGAGE IN GOOD SHAPE?</p>
    </header>
    <div class="dark-panel"></div>
    <h1 class="health-copy health-copy__title">FREE &amp; QUICK</h1>
    <p class="health-copy health-copy__check">MORTGAGE HEALTH CHECK</p>
    <div class="rule" style="left:41px;width:476px;top:380px"></div>
    <p class="health-copy health-copy__kicker">THE BRISK LOANS</p>
    <h2 class="health-copy health-copy__edge">EDGE</h2>
    <div class="rule" style="left:41px;width:476px;top:524px"></div>
    <ul class="edge-list">
      <li class="edge-item">
        <svg viewBox="0 0 88 88" aria-hidden="true"><circle cx="44" cy="44" r="42" fill="var(--brand-red)" stroke="#fff" stroke-width="3"/><g fill="#fff"><circle cx="30" cy="32" r="7"/><circle cx="58" cy="32" r="7"/><circle cx="44" cy="36" r="9"/><path d="M18 56c0-9 5-14 12-14s10 4 10 4-8 4-8 14z"/><path d="M70 56c0-9-5-14-12-14s-10 4-10 4 8 4 8 14z"/><path d="M28 64c0-11 7-18 16-18s16 7 16 18z"/></g></svg>
        Assess over<br>30 lenders
      </li>
      <li class="edge-item">
        <svg viewBox="0 0 88 88" aria-hidden="true"><circle cx="44" cy="44" r="42" fill="var(--brand-red)" stroke="#fff" stroke-width="3"/><circle cx="44" cy="44" r="24" fill="#fff"/><path d="M33 44l8 8 15-16" fill="none" stroke="var(--brand-red)" stroke-width="6" stroke-linecap="round" stroke-linejoin="round"/></svg>
        Quick<br>Approval
      </li>
      <li class="edge-item">
        <svg viewBox="0 0 88 88" aria-hidden="true"><circle cx="44" cy="44" r="42" fill="var(--brand-red)" stroke="#fff" stroke-width="3"/><circle cx="44" cy="44" r="28" fill="#fff"/><text x="44" y="57" text-anchor="middle" font-family="Montserrat,sans-serif" font-weight="800" font-size="38" fill="var(--brand-red)">$</text></svg>
        Free<br>Service
      </li>
      <li class="edge-item">
        <svg viewBox="0 0 88 88" aria-hidden="true"><circle cx="44" cy="44" r="42" fill="var(--brand-red)" stroke="#fff" stroke-width="3"/><g fill="none" stroke="#fff" stroke-width="5" stroke-linecap="round"><path d="M22 44a22 22 0 0 1 22-22"/><path d="M66 44a22 22 0 0 1-22 22"/></g><path d="M16 40l6 10 7-9z" fill="#fff"/><path d="M72 48l-6-10-7 9z" fill="#fff"/><circle cx="56" cy="28" r="9" fill="#fff"/><text x="56" y="33" text-anchor="middle" font-family="Montserrat,sans-serif" font-weight="800" font-size="13" fill="var(--brand-red)">$</text><circle cx="32" cy="60" r="8" fill="#fff"/></svg>
        Brisk Cost<br>Refund
      </li>
    </ul>
    <div class="lenders-band"></div>
    <div class="lenders-pill">WE ASSESS OVER 30 LENDERS</div>
    <ul class="lender-grid">
      <li class="lender">Orbit Direct</li><li class="lender">Westvale Bank</li><li class="lender">Meadow Bank</li><li class="lender">Sunridge Bank</li><li class="lender">Wattle Bank</li>
      <li class="lender">Harbour Permanent</li><li class="lender">Cityline Bank</li><li class="lender">Homestead Loans</li><li class="lender">Paprika Lending</li><li class="lender">Blueprint Lending</li>
      <li class="lender">Commonfield Bank</li><li class="lender">Riverton Bank</li><li class="lender">Austral Bank</li><li class="lender">Northgate Bank</li><li class="lender">Legacy Bank</li>
    </ul>
    <footer class="footer">www.briskloansdemo.com.au</footer>
  </section>

</main>
</body>
</html>
```